Business Card Design

We are a state licensed general contractor on the south east coast of Florida. We are a remodeling and home repairs business that have been in business for 14 years. Since we are located on the coast and our business name is Ridgeline Builders of Pine Hollow, Inc, we would like a "Ridgeline" themed design that would appeal to more affluent customers. I would like to see light blue colors with waves incorporated into the design. I would also like the design to communicate a modern, confident, responsible company character.

Industry/Entity Type

Contractor

Contact Information for Business Card

Tim Wexler 555-274-9183

```html
<!DOCTYPE html>
<html lang="en">
<head>
<meta charset="utf-8">
<title>Ridgeline Builders – Business Card</title>
<link href="https://fonts.googleapis.com/css2?family=Exo+2:wght@400;500;600&display=swap" rel="stylesheet">
<style>
  :root {
    --navy: #123a78;
    --navy-deep: #0c2c63;
    --sky: #3c9ad8;
    --paper: #ffffff;
    --paper-shade: #e9ecef;
    --ink: #2f3a48;
    --stage: #d9dde2;
  }
  * { margin: 0; padding: 0; box-sizing: border-box; }
  html, body { width: 1200px; height: 899px; overflow: hidden; }
  body {
    background: var(--stage);
    font-family: "Exo 2", sans-serif;
    display: flex; align-items: center; justify-content: center;
  }
  .card {
    position: relative;
    width: 1000px; height: 572px;
    border-radius: 48px;
    overflow: hidden;
    background: linear-gradient(180deg, var(--paper) 40%, var(--paper-shade) 100%);
    box-shadow: 0 18px 40px rgba(0,0,0,.18);
  }
  .card__waves { position: absolute; inset: 0; width: 100%; height: 100%; }
  .holder {
    position: absolute; right: 56px; top: 64px;
    text-align: right; color: var(--paper);
  }
  .holder__name { font-size: 36px; font-weight: 600; letter-spacing: 2px; text-transform: uppercase; }
  .holder__title { font-size: 24px; font-weight: 500; margin-top: 4px; }
  .contacts {
    position: absolute; left: 40px; top: 266px;
    list-style: none; color: var(--ink); font-size: 17px;
  }
  .contacts li { display: flex; align-items: center; gap: 12px; height: 30px; }
  .contacts svg { width: 16px; height: 16px; fill: var(--navy); flex: none; }
  .brand {
    position: absolute; left: 410px; top: 300px;
    display: flex; align-items: center; gap: 16px;
  }
  .brand__dot { width: 26px; height: 26px; border-radius: 50%; background: var(--sky); }
  .brand__name { font-size: 76px; font-weight: 600; color: var(--navy); letter-spacing: 1px; }
  .address {
    position: absolute; right: 60px; bottom: 54px;
    text-align: right; color: var(--ink); font-size: 21px; line-height: 1.35;
  }
</style>
</head>
<body>
  <article class="card">
    <svg class="card__waves" viewBox="0 0 1000 572" preserveAspectRatio="none" aria-hidden="true">
      <path d="M0,0 H1000 V268 C780,110 380,70 0,150 Z" fill="var(--navy)"/>
      <path d="M0,168 C380,92 760,132 1000,296 V276 C780,122 380,80 0,152 Z" fill="var(--sky)"/>
      <path d="M0,176 C380,104 760,148 1000,312 V300 C760,140 380,98 0,170 Z" fill="var(--sky)" opacity=".35"/>
    </svg>

    <header class="holder">
      <h1 class="holder__name">Tim Wexler</h1>
      <p class="holder__title">Managing Director</p>
    </header>

    <ul class="contacts">
      <li><svg viewBox="0 0 16 16"><path d="M3 1l3 3-2 2c1 2 3 4 5 5l2-2 3 3-2 3C6 14 2 10 1 3z"/></svg>555-274-9183</li>
      <li><svg viewBox="0 0 16 16"><path d="M4 0h8v16H4zM5.5 2v10h5V2z"/></svg>555-274-9184</li>
      <li><svg viewBox="0 0 16 16"><path d="M4 1h8v4H4zM1 6h14v7h-3v2H4v-2H1zM5 11v3h6v-3z"/></svg>555-274-9185</li>
      <li><svg viewBox="0 0 16 16"><path d="M1 3h14v10H1zM2.5 4.5L8 9l5.5-4.5v-.2H2.5z"/></svg>tim@ridgelinebuilders.com</li>
      <li><svg viewBox="0 0 16 16"><path d="M8 1a7 7 0 100 14A7 7 0 008 1zm0 2a5 5 0 110 10A5 5 0 018 3z"/></svg>www.ridgelinebuilders.com</li>
    </ul>

    <div class="brand">
      <span class="brand__dot"></span>
      <span class="brand__name">Ridgeline</span>
    </div>

    <address class="address" style="font-style:normal">
      214 Harbor St, Suite 6<br>Pine Hollow, FL
    </address>
  </article>
</body>
</html>
```